Tandle Repair - Handyman and Home Repair Services

I need a business card/letterhead logo for my new handyman service in my local area. I'm happy for a logo design to be done prior to business card design so it can be incorporated on to the card, for which I'd be happy to pay more for. I'd like it to be modern and not using the typical pictures of tools and cartoon characters in dungarees! I like the idea of tools but in a more modern way i.e subtle background images in different shades to main colour. I do like the american retro designs and those that show age and patina for example, having an image half old, half new in its appearance to represent the repairing of things. Colours in mind are 1950's retro colours, ie using grey with pastel greens, red and cream. I'd like to break the mould and the stigma thats attached to these jobs and make it more cool and up to date. I hope this will attract interior designers and more modern businesses to use my services.

This is the logo design I like and would be happy for this idea and colours:

http://toast-a-roam.co.uk/wp-content/uploads/2011/01/t-r_logo600px.png

```html
<!DOCTYPE html>
<html lang="en">
<head>
<meta charset="utf-8">
<title>Tandle Repair – Business Card</title>
<link rel="stylesheet" href="https://fonts.googleapis.com/css2?family=Big+Shoulders+Display:wght@600;700&display=swap">
<style>
  :root {
    --page: #ffffff;
    --card: #a3bf7e;
    --patina: #cfe0b8;
    --ink: #0a0a0a;
    --brand: #0d5a3a;
    --link: #1a1acc;
  }
  * { margin: 0; padding: 0; box-sizing: border-box; }
  html, body {
    width: 1200px;
    height: 1000px;
    overflow: hidden;
    background: var(--page);
  }
  .sheet {
    position: relative;
    width: 1200px;
    height: 1000px;
  }
  .card {
    position: absolute;
    left: 237px;
    width: 720px;
    height: 465px;
    background: var(--card);
    overflow: hidden;
    font-family: "Big Shoulders Display", "Arial Narrow", sans-serif;
    text-align: center;
  }
  .card--front { top: 23px; }
  .card--back  { top: 513px; }

  .brand-name {
    position: absolute;
    left: 0;
    right: 0;
    font-weight: 700;
    font-size: 96px;
    line-height: 1;
    color: var(--brand);
    letter-spacing: 1px;
  }
  .card--front .brand-name { top: 100px; }
  .card--back  .brand-name { top: 140px; }

  .condensed {
    display: inline-block;
    white-space: nowrap;
    transform-origin: center center;
  }

  .contact-line {
    position: absolute;
    left: 0;
    right: 0;
    top: 308px;
    font-weight: 600;
    font-size: 68px;
    line-height: 1;
    color: var(--ink);
  }
  .contact-line .condensed { transform: scaleX(0.64); }

  .web-address {
    position: absolute;
    left: 0;
    right: 0;
    top: 392px;
    font-weight: 600;
    font-size: 56px;
    line-height: 1;
    color: var(--link);
  }
  .web-address .condensed { transform: scaleX(0.63); }

  .patina-texture {
    position: absolute;
    left: 20px;
    top: 20px;
    width: 300px;
    height: 300px;
    border-radius: 50%;
    background: radial-gradient(circle at 45% 45%, var(--patina) 0%, var(--patina) 45%, rgba(207,224,184,0) 72%);
  }
  .tagline {
    position: absolute;
    left: -200px;
    right: -200px;
    top: 352px;
    font-weight: 600;
    font-size: 74px;
    line-height: 1;
    color: var(--ink);
    white-space: nowrap;
  }
  .tagline .condensed { transform: scaleX(0.67); }
</style>
</head>
<body>
  <main class="sheet">
    <section class="card card--front" aria-label="Card front">
      <h1 class="brand-name">Tandle Repair</h1>
      <p class="contact-line"><span class="condensed">Graham Pell 07700 900412</span></p>
      <p class="web-address"><span class="condensed">www.tandlerepair.co.uk</span></p>
    </section>

    <section class="card card--back" aria-label="Card back">
      <div class="patina-texture" role="img" aria-label="Faded distressed patina texture"></div>
      <h2 class="brand-name">Tandle Repair</h2>
      <p class="tagline"><span class="condensed">Handyman Services from Repair to Install</span></p>
    </section>
  </main>
</body>
</html>
```